Business cards and stationary for a health and wellbeing company
Lumen Forms
Business cards and stationary for a health and wellbeing company - Health
Creative Brief
Bright & Fun-filled
Jolene prescott
Director
PO Box
sales@lumenforms.com.au
www.lumenforms.com.au
Hi, I am happy to have a wide selection of fonts and designs. Lumen Forms is a health conscious Australian business that sells protein, supplements, health equipment, meditation and beauty products. We pride ourselves on great customer service, great products and a true passion for feeling and looking good. Our target market is females aged 18-60 years of age, mums and woman who want to feel amazing. Colour • Pink • White • Blue • Purple
Im open to different designs.
JolenePrescott JolenePrescott
Hi Everyone, Thank you so much for your great designs! I love the bright colours and lines that flow rather than straight and sharp. Could you please show me the front as well as the back of the business cards. I am wanting to change the font on my logo? I am wanting it so that the word Lumen sits above the word forms. Looking forward to some great designs! Thanks!

```html
<!DOCTYPE html>
<html lang="en">
<head>
<meta charset="utf-8">
<title>Lumen Forms – Business Card</title>
<link href="https://fonts.googleapis.com/css2?family=Dosis:wght@400;600;700&family=Oswald:wght@400;500&display=swap" rel="stylesheet">
<style>
  :root {
    --page: #e9e7ea;
    --card-top: #f7f7f8;
    --card-mid: #ececee;
    --magenta: #c23cbc;
    --magenta-light: #e07ad9;
    --magenta-dark: #a62ba0;
    --white: #ffffff;
    --ink: #4a4a52;
    --strip: #d9d9dd;
    --strip-dark: #8f8f97;
    --brand: #c23cbc;
  }
  * { box-sizing: border-box; margin: 0; padding: 0; }
  html, body { width: 1200px; height: 770px; overflow: hidden; }
  body {
    background: var(--page);
    font-family: "Dosis", sans-serif;
    position: relative;
  }
  .card {
    position: absolute;
    left: 100px; top: 70px;
    width: 1000px; height: 630px;
    border-radius: 10px;
    overflow: hidden;
    background: linear-gradient(180deg, var(--card-top) 0%, var(--card-mid) 100%);
    box-shadow: 0 12px 40px rgba(60, 40, 70, 0.18);
  }
  .brand {
    position: absolute;
    top: 95px; left: 0; right: 0;
    display: flex; align-items: center; justify-content: center;
    gap: 22px;
  }
  .brand-dot {
    width: 78px; height: 78px; border-radius: 50%;
    background: var(--magenta);
  }
  .brand-name {
    font-family: "Dosis", sans-serif;
    font-weight: 700;
    font-size: 72px;
    color: var(--brand);
    letter-spacing: -0.5px;
  }
  .band {
    position: absolute;
    left: 0; right: 0; top: 262px; height: 248px;
    background: linear-gradient(180deg, var(--magenta-light) 0%, var(--magenta) 18%, var(--magenta) 80%, var(--magenta-dark) 100%);
    display: grid;
    grid-template-columns: 1fr 1fr 1fr;
    color: var(--white);
  }
  .band::before {
    content: "";
    position: absolute; left: 0; right: 0; top: 14px; height: 3px;
    background: rgba(255,255,255,0.35);
  }
  .contact {
    display: flex; flex-direction: column; align-items: center;
    padding-top: 40px;
    text-align: center;
  }
  .icon {
    width: 86px; height: 86px; border-radius: 50%;
    background: rgba(255,255,255,0.22);
    border: 3px solid rgba(255,255,255,0.6);
    display: flex; align-items: center; justify-content: center;
    margin-bottom: 18px;
  }
  .icon svg { width: 46px; height: 46px; }
  .person-name {
    font-family: "Oswald", sans-serif;
    font-weight: 400;
    font-size: 40px;
    line-height: 1;
    letter-spacing: 1px;
  }
  .person-role {
    font-family: "Oswald", sans-serif;
    font-size: 13px;
    letter-spacing: 1.5px;
    margin-top: 6px;
  }
  .detail {
    font-size: 22px;
    font-weight: 400;
    line-height: 1.3;
  }
  .social {
    position: absolute;
    left: 0; right: 0; top: 510px; height: 120px;
    background: linear-gradient(180deg, #f1f1f3 0%, var(--strip) 100%);
    display: flex; align-items: center;
    padding-left: 48px;
    gap: 80px;
  }
  .social::after {
    content: "";
    position: absolute; left: 0; right: 0; bottom: 0; height: 22px;
    background: var(--strip-dark);
  }
  .follow {
    color: var(--ink);
    margin-top: -20px;
  }
  .follow-title {
    font-family: "Oswald", sans-serif;
    font-size: 30px;
    letter-spacing: 3px;
    line-height: 1;
  }
  .follow-sub {
    font-size: 12px;
    letter-spacing: 1.5px;
    margin-top: 4px;
  }
  .social-links {
    display: flex; gap: 26px;
    margin-top: -20px;
  }
  .social-link {
    width: 30px; height: 30px; border-radius: 50%;
    background: var(--ink);
  }
</style>
</head>
<body>
  <main class="card">
    <div class="brand">
      <span class="brand-dot"></span>
      <span class="brand-name">Lumen Forms</span>
    </div>

    <section class="band">
      <div class="contact">
        <span class="icon">
          <svg viewBox="0 0 48 48" fill="none" stroke="#fff" stroke-width="3">
            <circle cx="24" cy="17" r="8"/>
            <path d="M9 42c0-9 7-14 15-14s15 5 15 14"/>
          </svg>
        </span>
        <div class="person-name">DANA WHITLOW</div>
        <div class="person-role">GENERAL MANAGER</div>
      </div>
      <div class="contact">
        <span class="icon">
          <svg viewBox="0 0 48 48" fill="none" stroke="#fff" stroke-width="2.6">
            <circle cx="24" cy="24" r="18"/>
            <ellipse cx="24" cy="24" rx="8" ry="18"/>
            <path d="M6 24h36M9 15h30M9 33h30"/>
          </svg>
        </span>
        <div class="detail">sales@lumenforms.com.au</div>
        <div class="detail">www.lumenforms.com.au</div>
      </div>
      <div class="contact">
        <span class="icon">
          <svg viewBox="0 0 48 48" fill="none" stroke="#fff" stroke-width="3">
            <rect x="14" y="5" width="20" height="38" rx="4"/>
            <path d="M20 10h8"/>
            <circle cx="24" cy="37" r="1.8" fill="#fff"/>
          </svg>
        </span>
        <div class="detail">013 246 8579</div>
        <div class="detail">013 246 8579</div>
      </div>
    </section>

    <footer class="social">
      <div class="follow">
        <div class="follow-title">FOLLOW US</div>
        <div class="follow-sub">ON SOCIAL NETWORKS</div>
      </div>
      <div class="social-links">
        <span class="social-link"></span>
        <span class="social-link"></span>
        <span class="social-link"></span>
        <span class="social-link"></span>
      </div>
    </footer>
  </main>
</body>
</html>
```